Boutique Recruiting Firm Needs Eye-Catching Business Cards (and potentially new logo)!

I run a recruiting company in Charleston, South Carolina. I have a ton of networking events coming up and need business cards to grab potential clients attention.

I currently have a logo but if you want to try and recreate the logo to something more modern I am open to that. If you do decide to create a new logo please submit the business card with the old logo and the new one.

Staffing Under Blue Lanterns, LLC is the name of my company. I create videos to my clients and candidates which allows me to standout from my competition so I would like a business card (and possibly new logo) to do the same.

I do not specialize in any one industry of recruiting.

```html
<!DOCTYPE html>
<html lang="en">
<head>
<meta charset="utf-8">
<title>Staffing Under Blue Lanterns – Business Card</title>
<link rel="stylesheet" href="https://fonts.googleapis.com/css2?family=Michroma&display=swap">
<style>
  :root {
    --backdrop: #6b7583;
    --teal: #19bf98;
    --accent-red: #ff0000;
    --brown: #493935;
    --cream: #ecdcbf;
    --cream-fold: #d4c1a0;
    --ink: #111111;
  }
  * { margin: 0; padding: 0; box-sizing: border-box; }
  html, body {
    width: 1200px;
    height: 675px;
    overflow: hidden;
    background: var(--backdrop);
  }
  .card {
    position: absolute;
    left: 75px;
    top: 37.5px;
    width: 1050px;
    height: 600px;
    background: var(--teal);
    overflow: hidden;
    font-family: "Michroma", sans-serif;
    box-shadow: 0 10px 30px rgba(0,0,0,0.35);
  }
  .card-shapes {
    position: absolute;
    inset: 0;
  }
  .company-name {
    position: absolute;
    left: 95px;
    top: 300px;
    color: var(--ink);
    font-size: 31px;
    line-height: 1.45;
    letter-spacing: 0.5px;
  }
  .person-name {
    position: absolute;
    left: 640px;
    top: 118px;
    color: var(--ink);
    font-size: 29px;
    letter-spacing: 0.5px;
    white-space: nowrap;
  }
  .person-title {
    position: absolute;
    left: 800px;
    top: 184px;
    color: var(--cream);
    font-size: 21px;
    letter-spacing: 1px;
  }
  .contact {
    position: absolute;
    color: var(--cream);
    font-size: 19px;
    letter-spacing: 0.5px;
    line-height: 48px;
    white-space: nowrap;
  }
  .contact-phone { left: 824px; top: 261px; }
  .contact-email { left: 799px; top: 336px; }
  .contact-web   { left: 776px; top: 411px; }
</style>
</head>
<body>
  <div class="card">
    <svg class="card-shapes" width="1050" height="600" viewBox="0 0 1050 600">
      <polygon class="panel-brown" points="830,0 1050,0 1050,600 660,600" fill="var(--brown)"/>
      <polygon class="stripe-red" points="780,0 830,0 660,600 610,600" fill="var(--accent-red)"/>
      <polygon class="banner-fold" points="640,165 760,165 760,200" fill="var(--cream-fold)"/>
      <rect class="name-banner" x="610" y="105" width="440" height="60" fill="var(--cream)"/>

      <g class="icon icon-phone" transform="translate(792,285)">
        <circle r="22" fill="var(--cream)"/>
        <path d="M-11,-9 q-2,10 8,19 q9,8 14,6 l2,-6 l-7,-5 l-4,3 q-6,-4 -8,-9 l3,-4 l-4,-8 z" fill="var(--brown)"/>
      </g>
      <g class="icon icon-email" transform="translate(767,360)">
        <circle r="22" fill="var(--cream)"/>
        <rect x="-11" y="-7" width="22" height="14" fill="none" stroke="var(--brown)" stroke-width="2"/>
        <polyline points="-11,-7 0,2 11,-7" fill="none" stroke="var(--brown)" stroke-width="2"/>
      </g>
      <g class="icon icon-web" transform="translate(744,435)">
        <circle r="22" fill="var(--cream)"/>
        <circle r="11" fill="none" stroke="var(--brown)" stroke-width="2"/>
        <ellipse rx="5" ry="11" fill="none" stroke="var(--brown)" stroke-width="2"/>
        <line x1="-11" y1="0" x2="11" y2="0" stroke="var(--brown)" stroke-width="2"/>
      </g>
    </svg>

    <p class="company-name">Staffing Under<br>Blue Lanterns, LLC</p>

    <p class="person-name">Dana Whitfield</p>
    <p class="person-title">Manager</p>

    <p class="contact contact-phone">843.555.0147</p>
    <p class="contact contact-email">info@sublue.com</p>
    <p class="contact contact-web">www.sublue.com</p>
  </div>
</body>
</html>
```